Mental Health Non-profit Website that takes donations

We are a faith friendly non profit mental health agency. We need an about us section, a section for taking donations, and a place to list all our therapists and a photo of them
Unfortunately, many of our neighbors in Ohio face mental health challenges which harm their quality of life. Thousands of Ohioans experience trauma, addiction, anxiety, and depression, and the negative outcomes of these experiences continue to grow. While we know that data-driven counseling can improve quality of life for those with mental health challenges, many face economic and social barriers to accessing this transformational care.
Lanterns of Calm crosses barriers to mental health care for Ohioans. We are a nonprofit team of counselors dedicated to employing best practices in modes accessible to people of all backgrounds. A trauma-informed, faith-sensitive methodology uniquely equips us to address holistic mental health challenges. Donor support and community partnerships allow us to meet and serve individuals who could not otherwise access professional care.

Please see our case for support below for more information.

Target Market(s)

Those seeking mental health therapy

Industry/Entity Type

Mental Health Non-profit

Coding

Coded - Design and coding required

Colors

Designer to choose colors to be used in the design.

Requirements
Must have
• Our logo colors of navy blue and gold, our logo, about us section, our mission section, a place to accept donations page for all of our therapists and their pictures, and a place for blog posts

```html
<!DOCTYPE html>
<html lang="en">
<head>
<meta charset="utf-8">
<title>Lanterns of Calm Behavioral Health</title>
<link href="https://fonts.googleapis.com/css2?family=Arimo:wght@400;500;600;700&display=swap" rel="stylesheet">
<style>
:root{
  --navy:#15152b;
  --gold:#b8901a;
  --gold-light:#f3ca3a;
  --gold-grad:linear-gradient(90deg,#b38a17 0%,#d8ac2a 55%,#f4cd3d 100%);
  --ink:#1b1b1b;
  --body:#4a4a4a;
  --grey-band:#e6e6e6;
  --card-grey:#ececec;
  --white:#ffffff;
}
*{box-sizing:border-box;margin:0;padding:0}
html,body{width:1200px;height:4630px;overflow:hidden}
body{font-family:"Arimo",Arial,sans-serif;color:var(--ink);background:var(--white);position:relative}
section,header,footer{position:absolute;left:0;width:1200px}
.abs{position:absolute}
.btn{position:absolute;display:flex;align-items:center;justify-content:center;background:var(--gold-grad);color:var(--navy);font-weight:700;font-size:14px;border-radius:5px}
.section-title{position:absolute;left:0;width:1200px;text-align:center;font-weight:600;font-size:37px;color:var(--ink)}
.para{position:absolute;text-align:justify;text-align-last:center;font-size:13.5px;line-height:24px;color:var(--body)}

/* header */
.site-header{top:0;height:79px;background:var(--navy)}
.brand{left:144px;top:14px;display:flex;align-items:center;gap:8px;color:var(--gold-light);font-weight:700;font-size:13px;line-height:15px}
.brand-dot{width:22px;height:22px;border-radius:50%;background:var(--gold)}
.main-nav{left:381px;top:29px;display:flex;gap:20px;font-size:14.5px;color:var(--white)}
.main-nav .active{color:var(--gold-light)}
.donate-top{left:808px;top:18px;width:123px;height:43px}
.social{top:27px;width:26px;height:26px;border-radius:50%;border:1.5px solid var(--gold)}

/* hero */
.hero{top:79px;height:521px}
.hero-photo{position:absolute;inset:0;background:linear-gradient(100deg,#f5f3ee 0%,#e9e4dc 30%,#b9a48e 55%,#7a6a66 75%,#3e3a45 100%)}
.hero-welcome{left:144px;top:164px;font-size:24px;color:var(--gold)}
.hero-title{left:144px;top:197px;font-size:39px;line-height:49px;font-weight:700;color:var(--navy)}
.support{left:144px;top:305px;width:124px;height:42px}
.hero-arrow{top:427px;width:36px;height:36px;border-radius:50%;border:1.5px solid var(--navy);background:var(--white);display:flex;align-items:center;justify-content:center}

/* therapies */
.therapies{top:600px;height:584px}
.therapy-img{top:136px;width:280px;height:214px}
.therapy-card{top:320px;width:230px;height:172px;background:var(--card-grey);text-align:center;padding-top:22px}
.therapy-card h3{font-size:18px;font-weight:700;margin-bottom:10px}
.therapy-card p{font-size:13.5px;line-height:22px;color:var(--body);padding:0 20px}
.therapy-card.featured{background:linear-gradient(90deg,#b38a17,#f6e7a8)}
.therapy-card.featured p{color:#3a2c05}
.circle-arrow{top:475px;width:36px;height:36px;border-radius:50%;background:var(--white);border:1.5px solid var(--navy);display:flex;align-items:center;justify-content:center}
.circle-arrow.gold{background:var(--gold);border-color:var(--gold)}

/* about */
.about{top:1184px;height:479px;background:var(--navy)}
.about-bar{left:144px;top:97px;width:7px;height:307px;background:var(--gold)}
.about-title{left:183px;top:95px;font-size:40px;font-weight:600;color:var(--white)}
.about-text{left:183px;top:145px;width:450px;font-size:13.5px;line-height:24px;color:var(--white);text-align:justify}
.about-photo{left:677px;top:91px;width:379px;height:571px;background:linear-gradient(160deg,#a9a6a0 0%,#7f8aa0 40%,#8b7a6c 70%,#5b5650 100%)}
.hotline{top:1690px;left:225px;width:454px;height:124px;background:var(--gold-grad);display:flex;align-items:center;padding-left:44px;gap:22px}
.hotline-icon{width:62px;height:62px;border-radius:50%;border:2px solid rgba(255,255,255,.75);display:flex;align-items:center;justify-content:center}
.hotline p{color:var(--white);font-size:23px;font-weight:600;line-height:35px}
.play-box{top:1690px;left:679px;width:136px;height:124px;background:var(--white);display:flex;align-items:center;justify-content:center}

/* mission */
.mission{top:1814px;height:442px}
.learn{left:537px;top:302px;width:124px;height:43px}

/* stats */
.stats{top:2256px;height:319px;background:var(--gold-grad)}
.stat{top:0;width:270px;text-align:center;color:var(--white)}
.stat-ring{position:absolute;left:83px;top:54px;width:104px;height:104px;border-radius:50%;background:#f7ead0;border:6px solid #f5f0e0;display:flex;align-items:center;justify-content:center}
.stat-label{position:absolute;top:170px;width:270px;font-size:20px}
.stat-num{position:absolute;top:204px;width:270px;font-size:39px}
.stat-num.bold{font-weight:700}
.stat-divider{top:70px;width:1px;height:176px;background:rgba(255,255,255,.7)}

/* therapists */
.therapists{top:2575px;height:570px}
.therapist{top:162px;width:210px;text-align:center}
.therapist-photo{width:210px;height:244px;position:relative}
.therapist h3{font-size:19px;font-weight:700;margin-top:16px}
.therapist p{font-size:15px;color:var(--body);margin-top:6px}
.therapist.active h3{color:var(--gold)}
.profile-dot{position:absolute;left:80px;top:96px;width:50px;height:50px;border-radius:50%;background:var(--gold)}

/* blog */
.blog{top:3145px;height:675px;background:var(--grey-band)}
.blog-card{top:140px;width:429px;height:447px;background:var(--white);box-shadow:0 4px 14px rgba(0,0,0,.12)}
.blog-img{width:429px;height:260px;position:relative}
.blog-card h3{font-size:19px;font-weight:700;margin:34px 0 0 32px}
.blog-date{display:flex;align-items:center;gap:8px;color:var(--gold);font-size:19px;margin:12px 0 0 32px}
.blog-card p{font-size:13.5px;line-height:24px;color:var(--body);margin:12px 40px 0 32px}
.share{position:absolute;left:180px;top:95px;width:70px;height:70px;border-radius:50%;background:var(--gold);display:flex;align-items:center;justify-content:center}
.blog-arrow{top:380px}

/* giving */
.giving{top:3820px;height:420px}
.donate-main{left:537px;top:282px;width:124px;height:43px}

/* footer */
.site-footer{top:4240px;height:390px;background:var(--navy);color:var(--white)}
.footer-head{font-size:19px;font-weight:700;line-height:27px}
.newsletter{left:144px;top:140px;width:270px;height:42px;border:1px solid #5a5a70;display:flex;align-items:center;justify-content:space-between;padding:0 14px 0 16px;font-size:12.5px}
.f-social{top:213px;width:24px;height:24px;border-radius:50%;background:#2a2a45}
.f-social.on{background:var(--gold)}
.contact-row{display:flex;gap:22px;margin-bottom:22px}
.contact-row b{display:block;font-size:14px;margin-bottom:8px}
.contact-row span{font-size:12px}
.links{font-size:14px;line-height:32px}
.links li{list-style:none;display:flex;align-items:center;gap:14px}
.copyright{left:0;top:336px;width:1200px;text-align:center;font-size:14px}
</style>
</head>
<body>

<header class="site-header">
  <div class="brand abs"><span class="brand-dot"></span><span>LANTERNS<br>OF CALM</span></div>
  <nav class="main-nav abs">
    <span class="active">Home</span><span>About</span><span>Services</span><span>Blog</span><span>Reviews</span><span>Contact</span>
  </nav>
  <div class="btn donate-top">Donate Now</div>
  <span class="social abs" style="left:966px"></span>
  <span class="social abs" style="left:996px"></span>
  <span class="social abs" style="left:1029px"></span>
</header>

<section class="hero">
  <div class="hero-photo" role="img" aria-label="Smiling counselor with a pen talking with a client across a table"></div>
  <p class="hero-welcome abs">Welcome To</p>
  <h1 class="hero-title abs">Lanterns Of Calm<br>Behavioral Health</h1>
  <div class="btn support">Support Us</div>
  <div class="hero-arrow abs" style="left:147px"><svg width="12" height="12" viewBox="0 0 12 12"><path d="M8 1L3 6l5 5" stroke="#15152b" stroke-width="2" fill="none"/></svg></div>
  <div class="hero-arrow abs" style="left:196px"><svg width="12" height="12" viewBox="0 0 12 12"><path d="M4 1l5 5-5 5" stroke="#15152b" stroke-width="2" fill="none"/></svg></div>
</section>

<section class="therapies">
  <h2 class="section-title" style="top:74px">Our Theraphys</h2>

  <div class="therapy-img abs" style="left:144px;background:linear-gradient(135deg,#c9c5bd,#6f7d95 60%,#3e4050)" role="img" aria-label="Two women in a counseling conversation"></div>
  <div class="therapy-card abs" style="left:169px"><h3>Lorem ipsum dolor</h3><p>Lorem ipsum dolor sit amet, consectetur adipiscing elit, sed do eiusmod</p></div>
  <div class="circle-arrow abs" style="left:266px"><svg width="10" height="10" viewBox="0 0 10 10"><path d="M3 1l4 4-4 4" stroke="#15152b" stroke-width="2" fill="none"/></svg></div>

  <div class="therapy-img abs" style="left:460px;background:linear-gradient(180deg,#5a4a4a 0%,#c9803a 55%,#f0a23a 75%,#2a1d16 100%)" role="img" aria-label="Hand holding a glowing brain at sunset"></div>
  <div class="therapy-card featured abs" style="left:485px"><h3>Lorem ipsum dolor</h3><p>Lorem ipsum dolor sit amet, consectetur adipiscing elit, sed do eiusmod</p></div>
  <div class="circle-arrow gold abs" style="left:582px"><svg width="10" height="10" viewBox="0 0 10 10"><path d="M3 1l4 4-4 4" stroke="#fff" stroke-width="2" fill="none"/></svg></div>

  <div class="therapy-img abs" style="left:776px;background:linear-gradient(135deg,#e8e8e6,#a9b2bd 55%,#5d6a7a)" role="img" aria-label="Therapist taking notes during a session"></div>
  <div class="therapy-card abs" style="left:801px"><h3>Lorem ipsum dolor</h3><p>Lorem ipsum dolor sit amet, consectetur adipiscing elit, sed do eiusmod</p></div>
  <div class="circle-arrow abs" style="left:898px"><svg width="10" height="10" viewBox="0 0 10 10"><path d="M3 1l4 4-4 4" stroke="#15152b" stroke-width="2" fill="none"/></svg></div>
</section>

<section class="about">
  <div class="about-bar abs"></div>
  <h2 class="about-title abs">About Us</h2>
  <p class="about-text abs">Lorem ipsum dolor sit amet, consectetur adipiscing elit, sed do eiusmod tempor incididunt ut labore et dolore magna aliqua. Ut enim ad minim veniam, quis nostrud exercitation ullamco laboris nisi ut aliquip ex ea commodo consequat. Duis aute irure dolor in reprehenderit in voluptate velit esse cillum dolore eu fugiat nulla pariatur. Excepteur sint occaecat cupidatat non proident, sunt in culpa qui officia deserunt mollit anim id est laborum.Lorem ipsum dolor sit amet, consectetur adipiscing elit, sed do eiusmod tempor incididunt ut labore et dolore magna aliqua. Ut enim ad minim veniam, quis nostrud exercitation ullamco laboris nisi ut aliquip ex ea commodo consequat. Duis aute irure dolor in reprehenderit in voluptate velit esse cillum</p>
  <div class="about-photo abs" role="img" aria-label="Two young people seated on chairs in a group support session"></div>
</section>

<div class="hotline abs">
  <div class="hotline-icon"><svg width="26" height="26" viewBox="0 0 24 24"><path d="M6.6 10.8a15 15 0 006.6 6.6l2.2-2.2a1 1 0 011-.25 11.4 11.4 0 003.6.57 1 1 0 011 1V20a1 1 0 01-1 1A17 17 0 013 4a1 1 0 011-1h3.5a1 1 0 011 1c0 1.250.2 2.450.57 3.570a1 1 0 01-.25 1z" fill="#fff"/></svg></div>
  <p>For any inquiries call the<br>Hotline: +1 555 014 2630</p>
</div>
<div class="play-box abs"><svg width="28" height="28" viewBox="0 0 28 28"><path d="M4 2l22 12L4 26z" fill="#b8901a"/></svg></div>

<section class="mission">
  <h2 class="section-title" style="top:106px">Our Mission</h2>
  <p class="para" style="left:201px;top:164px;width:798px">Lorem ipsum dolor sit amet, consectetur adipiscing elit, sed do eiusmod tempor incididunt ut labore et dolore magna aliqua. Ut enim ad minim veniam, quis nostrud exercitation ullamco laboris nisi ut aliquip ex ea commodo consequat. Duis aute irure dolor in reprehenderit in voluptate velit esse cillum dolore eu fugiat nulla pariatur. Excepteur sint occaecat cupidatat non proident, sunt in culpa qui officia deserunt mollit anim id est laborum.Lorem ipsum dolor sit amet, consectetur adipiscing elit, sed do eiusmod tempor incididunt ut labore et dolore magna aliqua.</p>
  <div class="btn learn">Learn More</div>
</section>

<section class="stats">
  <div class="stat abs" style="left:50px"><div class="stat-ring"><svg width="44" height="44" viewBox="0 0 44 44" fill="none" stroke="#b8901a" stroke-width="2"><circle cx="14" cy="12" r="5"/><circle cx="30" cy="12" r="5"/><path d="M4 32c2-8 8-10 10-10s8 2 10 10M20 32c2-8 8-10 10-10s8 2 10 10"/></svg></div><p class="stat-label">Clients</p><p class="stat-num bold">5493</p></div>
  <div class="stat-divider abs" style="left:322px"></div>
  <div class="stat abs" style="left:321px"><div class="stat-ring"><svg width="44" height="44" viewBox="0 0 44 44" fill="none" stroke="#b8901a" stroke-width="2"><path d="M6 26l10-10 8 4 14-10M6 34h32"/><circle cx="22" cy="10" r="4"/></svg></div><p class="stat-label">Volunteer</p><p class="stat-num">1750</p></div>
  <div class="stat-divider abs" style="left:597px"></div>
  <div class="stat abs" style="left:591px"><div class="stat-ring"><svg width="44" height="44" viewBox="0 0 44 44" fill="none" stroke="#b8901a" stroke-width="2"><rect x="10" y="6" width="22" height="30" rx="2"/><path d="M15 14h12M15 20h12M15 26h7"/><circle cx="31" cy="31" r="6"/></svg></div><p class="stat-label">Projects</p><p class="stat-num">2458</p></div>
  <div class="stat-divider abs" style="left:869px"></div>
  <div class="stat abs" style="left:862px"><div class="stat-ring"><svg width="44" height="44" viewBox="0 0 44 44" fill="none" stroke="#b8901a" stroke-width="2"><rect x="8" y="8" width="12" height="12" rx="2"/><rect x="24" y="8" width="12" height="12" rx="2"/><rect x="8" y="24" width="12" height="12" rx="2"/><rect x="24" y="24" width="12" height="12" rx="2"/></svg></div><p class="stat-label">Community</p><p class="stat-num">1670</p></div>
</section>

<section class="therapists">
  <h2 class="section-title" style="top:86px">Our Therapists</h2>
  <div class="therapist abs" style="left:144px"><div class="therapist-photo" style="background:linear-gradient(160deg,#9a9a98,#4e5f7a 60%,#2f3542)" role="img" aria-label="Portrait of therapist John Doe"></div><h3>John Doe</h3><p>Company name</p></div>
  <div class="therapist abs" style="left:378px"><div class="therapist-photo" style="background:linear-gradient(160deg,#6fa3d4,#cfd8df 55%,#f2f2f2)" role="img" aria-label="Portrait of therapist William"></div><h3>William</h3><p>Company name</p></div>
  <div class="therapist active abs" style="left:612px"><div class="therapist-photo" style="background:linear-gradient(160deg,#5c6470,#3f4a5a 60%,#2a2f38)" role="img" aria-label="Portrait of therapist Peter"><span class="profile-dot"></span></div><h3>Peter</h3><p>Company name</p></div>
  <div class="therapist abs" style="left:846px"><div class="therapist-photo" style="background:linear-gradient(160deg,#f0f0ee,#d9d6d2 60%,#bfb6ad)" role="img" aria-label="Portrait of therapist Alisa"></div><h3>Alisa</h3><p>Company name</p></div>
</section>

<section class="blog">
  <h2 class="section-title" style="top:68px">Latest Blog</h2>
  <svg class="abs blog-arrow" style="left:60px" width="16" height="26" viewBox="0 0 16 26"><path d="M13 2L3 13l10 11" stroke="#222" stroke-width="2.5" fill="none"/></svg>
  <svg class="abs blog-arrow" style="left:1118px" width="16" height="26" viewBox="0 0 16 26"><path d="M3 2l10 11L3 24" stroke="#222" stroke-width="2.5" fill="none"/></svg>

  <article class="blog-card abs" style="left:144px">
    <div class="blog-img" style="background:linear-gradient(120deg,#e3e1dc,#9aa3b0 45%,#5f6b4e 80%,#3c4434)" role="img" aria-label="Older man in conversation with a younger man">
      <span class="share"><svg width="26" height="22" viewBox="0 0 26 22"><path d="M15 1l10 9-10 9v-5C8 14 4 16 1 21c1-8 5-13 14-14z" fill="#fff"/></svg></span>
    </div>
    <h3>Lorem ipsum dolor sit amet</h3>
    <div class="blog-date"><svg width="18" height="18" viewBox="0 0 18 18" fill="none" stroke="#b8901a" stroke-width="1.6"><rect x="1.5" y="3" width="15" height="13.5" rx="1.5"/><path d="M1.5 7h15M5 1v4M13 1v4"/></svg>Nov 10,2024</div>
    <p>Lorem ipsum dolor sit amet, consectetur adipiscing elit, sed do eiusmod tempor incididunt ut labore et dolore magna aliqua.</p>
  </article>

  <article class="blog-card abs" style="left:627px">
    <div class="blog-img" style="background:linear-gradient(110deg,#f0b46a,#c47436 45%,#4a2d22 75%,#1e1614)" role="img" aria-label="Silhouette of a distressed person against a warm sunset"></div>
    <h3>Lorem ipsum dolor sit amet</h3>
    <div class="blog-date"><svg width="18" height="18" viewBox="0 0 18 18" fill="none" stroke="#b8901a" stroke-width="1.6"><rect x="1.5" y="3" width="15" height="13.5" rx="1.5"/><path d="M1.5 7h15M5 1v4M13 1v4"/></svg>Nov 10,2024</div>
    <p>Lorem ipsum dolor sit amet, consectetur adipiscing elit, sed do eiusmod tempor incididunt ut labore et dolore magna aliqua.</p>
  </article>
</section>

<section class="giving">
  <h2 class="section-title" style="top:82px">Giving Help to Those Who Need It</h2>
  <p class="para" style="left:201px;top:140px;width:798px">Lorem ipsum dolor sit amet, consectetur adipiscing elit, sed do eiusmod tempor incididunt ut labore et dolore magna aliqua. Ut enim ad minim veniam, quis nostrud exercitation ullamco laboris nisi ut aliquip ex ea commodo consequat. Duis aute irure dolor in reprehenderit in voluptate velit esse cillum dolore eu fugiat nulla pariatur. Excepteur sint occaecat cupidatat non proident, sunt in culpa qui officia deserunt mollit anim id est laborum.Lorem ipsum dolor sit amet, consectetur adipiscing elit, sed do eiusmod tempor incididunt ut labore et dolore magna aliqua.</p>
  <div class="btn donate-main">Donate Now</div>
</section>

<footer class="site-footer">
  <h4 class="footer-head abs" style="left:144px;top:70px">SUBSCRIBE TO<br>OUR NEWSLETTER</h4>
  <div class="newsletter abs"><span>Email address</span><svg width="16" height="14" viewBox="0 0 16 14"><path d="M1 7l14-6-4 12-3-5z" fill="#d8ac2a"/></svg></div>
  <span class="f-social abs" style="left:146px"></span>
  <span class="f-social on abs" style="left:178px"></span>
  <span class="f-social abs" style="left:210px"></span>

  <h4 class="footer-head abs" style="left:503px;top:70px">CONTACT INFO</h4>
  <div class="abs" style="left:503px;top:130px">
    <div class="contact-row"><svg width="16" height="20" viewBox="0 0 16 20"><path d="M8 0a7 7 0 017 7c0 5-7 13-7 13S1 12 1 7a7 7 0 017-7z" fill="#d8ac2a"/><circle cx="8" cy="7" r="2.5" fill="#15152b"/></svg><div><b>Address</b><span>Lorem ipsum dolor sit amet</span></div></div>
    <div class="contact-row"><svg width="18" height="14" viewBox="0 0 18 14"><rect width="18" height="14" rx="1.5" fill="#d8ac2a"/><path d="M1 1l8 6 8-6" stroke="#15152b" stroke-width="1.5" fill="none"/></svg><div><b>Email</b><span>hello@lanternsofcalm.org</span></div></div>
    <div class="contact-row"><svg width="16" height="16" viewBox="0 0 24 24"><path d="M6.6 10.8a15 15 0 006.6 6.6l2.2-2.2a1 1 0 011-.25 11.4 11.4 0 003.6.57 1 1 0 011 1V20a1 1 0 01-1 1A17 17 0 013 4a1 1 0 011-1h3.5a1 1 0 011 1c0 1.25.2 2.45.57 3.57a1 1 0 01-.25 1z" fill="#d8ac2a"/></svg><div><b>Phone</b><span>+1 555 014 2630</span></div></div>
  </div>

  <h4 class="footer-head abs" style="left:765px;top:70px">QUICK LINKS</h4>
  <ul class="links abs" style="left:765px;top:124px">
    <li><span style="color:#d8ac2a">»</span>Home</li><li><span style="color:#d8ac2a">»</span>About</li><li><span style="color:#d8ac2a">»</span>Services</li><li><span style="color:#d8ac2a">»</span>Contact</li>
  </ul>
  <ul class="links abs" style="left:900px;top:124px">
    <li><span style="color:#d8ac2a">»</span>Terms and Condition</li><li><span style="color:#d8ac2a">»</span>Privacy policy</li><li><span style="color:#d8ac2a">»</span>Help</li><li><span style="color:#d8ac2a">»</span>Support</li>
  </ul>

  <p class="copyright abs">© Copyrights 2024 | All Rights Reserved</p>
</footer>

</body>
</html>
```